Flight school sign for building, banner, and bilboard

This sign is primarily for use on the side of our flight school building to draw attention for current and future flight school students. We offer airplane and helicopter flight training, ground school training and seminars, airplane and helicopter rentals, multi-engine training, and more. I would like a professional but exciting sign that can be used across a multitude of signage options such as banners, banner ads, billboard, and other mediums so that our sign is consistent and recognizable.

Contact Information for Business Card

The business card should match our company sign somewhat but not exactly. We want good and exciting imagery or wording and energizing/exciting colors.

```html
<!DOCTYPE html>
<html lang="en">
<head>
<meta charset="utf-8">
<title>Meridian Aviation – Roll-up Banner</title>
<link rel="stylesheet" href="https://fonts.googleapis.com/css2?family=Fira+Sans+Condensed:wght@600;700&display=swap">
<style>
  :root {
    --navy: #0b1a3a;
    --red: #ee1c25;
    --white: #ffffff;
    --stage: #e6e7e9;
    --sky-top: #3d8fd6;
    --sky-mid: #b9d6ee;
    --cabin: #8a8f96;
  }
  * { margin: 0; padding: 0; box-sizing: border-box; }
  html, body { width: 1200px; height: 2391px; overflow: hidden; }
  body {
    background: var(--stage);
    font-family: "Fira Sans Condensed", "Arial Narrow", sans-serif;
    position: relative;
  }
  .banner {
    position: absolute;
    left: 110px; top: 44px;
    width: 980px; height: 2303px;
    background: var(--navy);
    overflow: hidden;
    box-shadow: 0 10px 40px rgba(0,0,0,0.25);
  }
  .banner-shapes { position: absolute; inset: 0; width: 100%; height: 100%; }
  .brand-name {
    position: absolute; left: 0; right: 0; top: 1068px;
    text-align: center; color: var(--white);
    font-weight: 600; font-size: 58px; letter-spacing: 3px; line-height: 66px;
    text-transform: uppercase;
  }
  .brand-tagline {
    position: absolute; left: 0; right: 0; top: 1128px;
    text-align: center; color: var(--white);
    font-weight: 600; font-size: 15px; letter-spacing: 2px;
    text-transform: uppercase;
  }
  .offer-heading {
    position: absolute; left: 0; right: 0; top: 1180px;
    text-align: center; color: var(--red);
    font-weight: 700; font-size: 58px; line-height: 62px;
    text-transform: uppercase;
  }
  .offer-item {
    position: absolute; left: 259px; width: 660px;
    color: var(--white); font-weight: 700;
    font-size: 52px; line-height: 71px;
  }
  .phone-pill {
    position: absolute; left: 190px; top: 2050px;
    width: 600px; height: 108px;
    background: var(--red);
    border: 5px solid var(--white);
    border-radius: 54px;
    display: flex; align-items: center;
    padding-left: 16px;
    color: var(--white); font-weight: 600; font-size: 64px;
  }
  .phone-pill .phone-icon { width: 68px; height: 68px; margin-right: 26px; flex: none; }
  .website {
    position: absolute; left: 0; right: 0; top: 2200px;
    display: flex; justify-content: center; align-items: center;
    color: var(--navy); font-weight: 700; font-size: 52px;
  }
  .website .globe-icon { width: 54px; height: 54px; margin-right: 14px; }
  .website .domain { color: var(--red); }
</style>
</head>
<body>
  <div class="banner">
    <svg class="banner-shapes" viewBox="0 0 454 1067" preserveAspectRatio="none">
      <defs>
        <linearGradient id="cockpit-tone" x1="0" y1="0" x2="0.6" y2="1">
          <stop offset="0" stop-color="#3d8fd6"/>
          <stop offset="0.45" stop-color="#b9d6ee"/>
          <stop offset="1" stop-color="#8a8f96"/>
        </linearGradient>
      </defs>
      <path class="swoosh" fill="var(--red)" stroke="var(--white)" stroke-width="1.5"
        d="M38,58 C70,290 190,412 292,410 C372,408 432,330 456,236 L456,140 L281,125 Z"/>
      <circle class="hero-photo" cx="281" cy="125" r="215" fill="url(#cockpit-tone)" stroke="var(--white)" stroke-width="2"
        role="img" aria-label="Photo of a smiling pilot with headset at the controls inside a cockpit, blue sky beyond the windshield"/>
      <line x1="55" y1="561" x2="155" y2="561" stroke="var(--white)" stroke-width="1"/>
      <line x1="298" y1="561" x2="398" y2="561" stroke="var(--white)" stroke-width="1"/>
      <g class="offer-icons" fill="var(--red)" stroke="var(--white)" stroke-width="1.5">
        <circle cx="66" cy="631" r="22"/>
        <circle cx="66" cy="720" r="22"/>
        <circle cx="66" cy="804" r="22"/>
        <circle cx="66" cy="893" r="22"/>
      </g>
      <g fill="none" stroke="var(--white)" stroke-width="1.2">
        <circle cx="66" cy="631" r="15"/>
        <path d="M56,641 L76,621 M62,624 L72,636 M58,634 L63,639"/>
        <rect x="57" y="711" width="18" height="12"/>
        <path d="M58,727 h16 M61,714 h10 M61,718 h7"/>
        <path d="M55,800 h16 a5,5 0 0 1 0,10 h-16 z M63,800 v-5 M54,795 h20"/>
        <circle cx="66" cy="893" r="12"/>
        <circle cx="66" cy="893" r="5"/>
        <path d="M66,881 v24 M54,893 h24"/>
      </g>
      <rect class="footer-band" x="0" y="982" width="454" height="85" fill="var(--white)"/>
    </svg>

    <div class="brand-name">Meridian Aviation</div>
    <div class="brand-tagline">Clear skies ahead, every flight counts</div>

    <h2 class="offer-heading">We Offer</h2>

    <p class="offer-item" style="top:1291px">Airplane and helicopter<br>flight training</p>
    <p class="offer-item" style="top:1483px">Ground school training<br>and seminars</p>
    <p class="offer-item" style="top:1664px">Airplane and<br>helicopter rentals</p>
    <p class="offer-item" style="top:1857px">Multi-engine training,<br>and more.</p>

    <div class="phone-pill">
      <svg class="phone-icon" viewBox="0 0 40 40" aria-hidden="true">
        <circle cx="20" cy="20" r="19" fill="var(--white)"/>
        <circle cx="20" cy="20" r="15" fill="var(--navy)"/>
        <path d="M14,11 l4,0 l1.5,5 l-2.5,2 a12,12 0 0 0 5,5 l2,-2.5 l5,1.5 l0,4 a2,2 0 0 1 -2,2 a18,18 0 0 1 -15,-15 a2,2 0 0 1 2,-2 z" fill="var(--white)"/>
      </svg>
      <span class="phone-number">(555) 201 7788</span>
    </div>

    <div class="website">
      <svg class="globe-icon" viewBox="0 0 40 40" aria-hidden="true">
        <circle cx="20" cy="20" r="18" fill="none" stroke="var(--navy)" stroke-width="3"/>
        <circle cx="20" cy="20" r="12" fill="var(--red)"/>
        <path d="M8,20 h24 M20,8 v24 M11,14 h18 M11,26 h18" stroke="var(--white)" stroke-width="1.3" fill="none"/>
        <ellipse cx="20" cy="20" rx="5" ry="12" fill="none" stroke="var(--white)" stroke-width="1.3"/>
      </svg>
      <span>www.<span class="domain">meridianaviation</span>.com</span>
    </div>
  </div>
</body>
</html>
```